River Stones, Evening Light Poster for American Indian Older Adults

We need am 11" x 17" poster designed for a health outreach project designed to reach older U.S. American Indians. The materials developed through this project will be distributed to American Indian and Alaska Native tribes, communities and tribal-serving organizations across the U.S. (more than 500 different tribes). If we find a successful design we will work with that designer to produce at least one other item we need design work for using the same look/feel and maybe other materials for this project. (more work!). The poster will include a set of facts (bulleted list on the attached document) that we would like presented in an "infographic" style. The design must be reflective of the American Indian culture and designed with older adults (65 and older) in mind. Imagery plays a strong role in the American Indian culture in the U.S. images of the heart, water, feathers, circle of life, etc. If you use photos of people they must include older adults and they must be American Indian (Native American). We prefer deep earth tones for the color scheme. The design must take into account design principles for older adults: 1. Try not to put colored font on colored background 2. Ensure high contrast for text 3. Font style should be sans serif, not cursive,decorative or heavily stylized because it is harder to read 4. Avoid using all caps 5. Don't print sideways or on top of images, shaded, backgrounds, etc. 6. All images should related specifically to the content of the text and be culturally appropriate for both older adults and American Indians. The final design should be easy to read and appeal to older American Indian adults. We need to incorporate three logos on the poster towards the bottom they should not be the center/focus of the poster. We also need to include a statement about who produced the materials- that can be very small below the logos at the bottom of the poster. We've attached the text for the poster and three logo files (note one is solid blue- we will finalize that after the document design is selected but need a placeholder for that logo.

Target Market(s)

Older adult (65 and older) American Indian and Alaska Natives and their family members in tribes, communities and tribal-serving organizations across the US

Font styles to use
Sans Serif

Requirements
Must have
• Must adhere to good design principles for older adults (listed in project description)
• Must feature culturally appropriate/targeted imagery and design look and feel

```html
<!DOCTYPE html>
<html lang="en">
<head>
<meta charset="utf-8">
<title>River Stones, Evening Light</title>
<link href="https://fonts.googleapis.com/css2?family=Jost:wght@400;500;600;800&display=swap" rel="stylesheet">
<style>
  :root {
    --paper: #eee9e1;
    --ink: #123a34;
    --ink-dark: #1c1c1c;
    --teal: #1f8a8a;
    --red: #c8202f;
    --brown: #5a3a22;
    --gold: #f5c02a;
    --blue: #1b6fc2;
    --green: #1aa24a;
    --orange: #e0671e;
    --white: #ffffff;
  }
  * { box-sizing: border-box; margin: 0; padding: 0; }
  html, body { width: 777px; height: 1200px; overflow: hidden; background: var(--paper); }
  body { font-family: "Jost", sans-serif; color: var(--ink-dark); }
  .poster { position: relative; width: 777px; height: 1200px; background: var(--paper); }

  .top-band {
    position: absolute; left: 0; top: 0; width: 777px; height: 30px;
    background: linear-gradient(180deg, var(--teal) 0 22%, var(--red) 22% 78%, var(--teal) 78% 100%);
  }
  .title {
    position: absolute; left: 60px; top: 66px;
    font-weight: 600; font-size: 50px; line-height: 1.3; color: var(--ink);
  }
  .heart-brain-art {
    position: absolute; left: 532px; top: 62px; width: 204px; height: 140px;
    border-radius: 50%;
    background: linear-gradient(90deg, #d8262b 0 48%, #f08a1f 52% 100%);
  }
  .gathering-photo {
    position: absolute; left: 0; top: 228px; width: 777px; height: 306px;
    background: linear-gradient(180deg, #c9dbe9 0%, #b9ccd8 35%, #6f8f4c 60%, #4c7d2f 100%);
  }
  .subhead {
    position: absolute; left: 50px; top: 560px;
    font-weight: 500; font-size: 27px; line-height: 1.3; color: var(--ink);
  }
  .fact {
    position: absolute; right: 227px; text-align: right;
    font-size: 23px; line-height: 1.25; color: var(--ink-dark);
  }
  .fact-1 { top: 664px; }
  .fact-2 { top: 748px; }
  .fact-3 { top: 806px; }
  .fact-4 { top: 892px; }

  .million-box {
    position: absolute; left: 566px; top: 663px; width: 112px; height: 55px;
    background: var(--gold);
  }
  .million-figures {
    position: absolute; left: 5px; top: 5px; width: 102px; height: 32px;
    background: linear-gradient(90deg, #ffffff 0 84%, #222 84% 100%); opacity: .85;
  }
  .million-label {
    position: absolute; left: 0; bottom: 2px; width: 100%; text-align: center;
    font-size: 11px; color: var(--ink-dark);
  }
  .cause-chart { position: absolute; left: 577px; top: 728px; }
  .cause-bar {
    height: 9px; margin-bottom: 1.8px; background: var(--blue);
    color: var(--white); font-size: 7px; line-height: 9px; padding-left: 5px; font-style: italic;
  }
  .elder-figures {
    position: absolute; left: 572px; top: 804px; width: 104px; height: 64px;
    background:
      linear-gradient(90deg, #1f3a33 0 19%, var(--red) 19% 100%) top / 100% 46% no-repeat,
      linear-gradient(var(--red), var(--red)) bottom / 100% 46% no-repeat;
  }
  .native-figures {
    position: absolute; left: 582px; top: 894px; width: 90px; height: 50px;
    background: linear-gradient(90deg, #3a3a3a 0 33%, var(--teal) 33% 100%);
  }
  .divider {
    position: absolute; left: 0; top: 970px; width: 777px; height: 7px;
    background: repeating-linear-gradient(90deg, var(--red) 0 5px, var(--brown) 5px 9px);
  }
  .risk-note {
    position: absolute; left: 55px; top: 985px; width: 440px;
    font-size: 23px; line-height: 1.23; color: var(--ink);
  }
  .call-box {
    position: absolute; left: 502px; top: 982px; width: 275px; height: 126px;
    background: #1a1a1a; color: var(--white);
    padding: 4px 12px 0 22px;
    font-weight: 800; font-size: 18.5px; line-height: 1.22;
  }
  .footer {
    position: absolute; left: 0; top: 1108px; width: 777px; height: 92px; background: var(--white);
  }
  .partner {
    position: absolute; display: flex; align-items: center; gap: 8px;
    font-weight: 600; font-size: 17px;
  }
  .partner-elders { left: 28px; top: 34px; color: var(--green); }
  .partner-elders .mark { width: 20px; height: 20px; background: var(--green); }
  .partner-riverbend { left: 386px; top: 34px; color: var(--orange); }
  .partner-placeholder {
    position: absolute; left: 670px; top: 18px; width: 82px; height: 60px;
    border: 1.5px solid var(--blue);
  }
</style>
</head>
<body>
<main class="poster">
  <div class="top-band" role="img" aria-label="Band of traditional geometric diamond pattern in teal, red and brown"></div>

  <h1 class="title">River Stones,<br>Evening Light…</h1>
  <div class="heart-brain-art" role="img" aria-label="Illustration of a red heart and an orange brain joined by circular arrows"></div>

  <div class="gathering-photo" role="img" aria-label="Photograph of American Indian elders in traditional regalia at an outdoor powwow on a grassy field"></div>

  <h2 class="subhead">The River of Life Flows Through the Heart,<br>Protecting the Mind and Body</h2>

  <p class="fact fact-1">5.7 million Americans have<br>Alzheimer’s disease</p>
  <div class="million-box">
    <div class="million-figures" role="img" aria-label="Row of six person pictograms"></div>
    <span class="million-label">5.7 Million</span>
  </div>

  <p class="fact fact-2">Alzheimer’s is the 6th leading cause of death</p>
  <div class="cause-chart">
    <div class="cause-bar" style="width:100px">1. Heart Disease</div>
    <div class="cause-bar" style="width:89px">2. Cancer</div>
    <div class="cause-bar" style="width:81px">3. Respiratory</div>
    <div class="cause-bar" style="width:73px">4. Accidents</div>
    <div class="cause-bar" style="width:67px">5. Diabetes</div>
    <div class="cause-bar" style="width:59px">6. ALZHEIMER</div>
  </div>

  <p class="fact fact-3">1 out 10 people age 65 and older<br>has Alzheimer’s</p>
  <div class="elder-figures" role="img" aria-label="Ten person pictograms, one dark and nine red"></div>

  <p class="fact fact-4">1 out of 3 American Indians over 65<br>develop dementia, including Alzheimer’s</p>
  <div class="native-figures" role="img" aria-label="Three person pictograms, one dark grey and two teal"></div>

  <div class="divider" role="img" aria-label="Beaded border pattern in red and brown"></div>

  <p class="risk-note">Elders with diabetes, heart disease, or high blood pressure have a much higher risk of developing Alzheimer’s or other dementias.</p>
  <p class="call-box">Make an appointment with your doctor today to talk about how to keep your mind and heart healthy.</p>

  <footer class="footer">
    <div class="partner partner-elders"><span class="mark"></span>Cedar Circle Elders Network</div>
    <div class="partner partner-riverbend">Riverbend Health Alliance</div>
    <div class="partner-placeholder"></div>
  </footer>
</main>
</body>
</html>
```